Elegant wine label

Looking for a new Napa Valley wine label called "Velmora". Our wines will retail for $150 + per bottle. Velmora is derived from the greek word Ergo (therefore) tied in with Air for aeration for wine.

We handcraft our small production wine. 200 cases.
Looking for a very sophisticated, minimalist elegant look. Wine labels we like for inspiration and reference include: www.tarvik.wine, www.pellunwine.com, www.morvadestates.com, www.quillbarrowwine.com, www.brevixestate.com/Wine, https://shop.lantivewine.com/wine

Colors will include white, black and blue foil (Approx. color: C 94.9, M 83.53, Y 0, K 0). We want a custom-created, minimal greek/roman looking font for lettering.

```html
<!DOCTYPE html>
<html lang="en">
<head>
<meta charset="utf-8">
<title>Velmora — Napa Valley Cabernet Sauvignon Label</title>
<link href="https://fonts.googleapis.com/css2?family=Cinzel:wght@500;600&family=Cormorant+Garamond:wght@500&family=Montserrat:wght@500&family=Pinyon+Script&family=Zilla+Slab:wght@700&display=swap" rel="stylesheet">
<style>
  :root {
    --glass-black: #050505;
    --gold-light: #f2cf5a;
    --gold-mid: #d9a52a;
    --gold-deep: #a8761a;
    --paper: #f1f0ee;
    --paper-shade: #e4e2df;
    --ink: #3a3a3a;
    --ink-soft: #6e6e6e;
    --blush: #e6c3c6;
    --hairline-gold: #c9a44c;
  }
  * { margin: 0; padding: 0; box-sizing: border-box; }
  html, body {
    width: 1200px; height: 1200px; overflow: hidden;
    background: var(--glass-black);
  }
  .label-face {
    position: relative; width: 1200px; height: 1200px;
    background: var(--glass-black);
  }
  .medallion {
    position: absolute; left: 390px; top: 150px;
    width: 420px; height: 420px; border-radius: 50%;
    background: radial-gradient(circle at 45% 35%, var(--gold-light) 0%, var(--gold-mid) 55%, var(--gold-deep) 100%);
  }
  .vintage {
    position: absolute; left: 0; right: 0; top: 660px; text-align: center;
  }
  .vintage-year {
    font-family: "Zilla Slab", serif; font-weight: 700;
    font-size: 46px; letter-spacing: 10px; padding-left: 10px;
    color: var(--gold-light); line-height: 1;
  }
  .vintage-word {
    font-family: "Montserrat", sans-serif; font-weight: 500;
    font-size: 12px; letter-spacing: 6px; padding-left: 6px;
    color: var(--gold-mid); margin-top: 8px;
  }
  .wine-label {
    position: absolute; left: 355px; top: 790px;
    width: 490px; height: 290px;
    background: linear-gradient(180deg, var(--paper) 0%, var(--paper-shade) 100%);
    clip-path: polygon(16px 0, calc(100% - 16px) 0, 100% 16px, 100% calc(100% - 16px), calc(100% - 16px) 100%, 16px 100%, 0 calc(100% - 16px), 0 16px);
  }
  .wine-label-frame {
    position: absolute; inset: 12px;
    border: 1px solid var(--hairline-gold);
  }
  .crest-area {
    position: absolute; left: 170px; top: 22px;
    width: 150px; height: 245px; border-radius: 50%;
    background: radial-gradient(ellipse at center, var(--blush) 0%, rgba(230,195,198,0.35) 50%, rgba(230,195,198,0) 75%);
    opacity: 0.7;
  }
  .label-text {
    position: relative; text-align: center; padding-top: 48px;
  }
  .region, .varietal {
    font-family: "Cormorant Garamond", serif; font-weight: 500;
    font-size: 13px; letter-spacing: 5px; color: var(--ink-soft); line-height: 1.35;
  }
  .brand-name {
    font-family: "Cinzel", serif; font-weight: 600;
    font-size: 58px; letter-spacing: 9px; padding-left: 9px;
    color: var(--ink); line-height: 1; margin-top: 18px;
  }
  .appellation {
    font-family: "Montserrat", sans-serif; font-weight: 500;
    font-size: 15px; letter-spacing: 8px; padding-left: 8px;
    color: var(--ink); margin-top: 10px;
  }
  .collection {
    font-family: "Pinyon Script", cursive;
    font-size: 28px; color: var(--hairline-gold); margin-top: 6px;
  }
</style>
</head>
<body>
  <main class="label-face">
    <div class="medallion" role="img" aria-label="Gold foil medallion with an engraved archer drawing a bow against a sunburst"></div>

    <div class="vintage">
      <div class="vintage-year">2025</div>
      <div class="vintage-word">VINTAGE</div>
    </div>

    <section class="wine-label">
      <div class="wine-label-frame"></div>
      <div class="crest-area" role="img" aria-label="Faint blush ornamental crest behind the lettering"></div>
      <div class="label-text">
        <p class="region">NAPA VALLEY</p>
        <p class="varietal">CABERNET SAUVIGNON</p>
        <h1 class="brand-name">VELMORA</h1>
        <p class="appellation">OAKVILLE</p>
        <p class="collection">Private Collection</p>
      </div>
    </section>
  </main>
</body>
</html>
```